Game, Voice & Dedicated Server Company Needs a Business Card Design

We need a new business card design, centered around our new logo (PSD provided below).

Designs that we do like:
https://pixelmarsh.net/item/corporate-business-card/5382017?s_rank=43 (needs to be made more eye catching)

Our main areas of business are:
- Dedicated Servers
- Game Servers
- Voice Servers
- Mitigation Security Specialists

Industry/Entity Type

Business

Contact Information for Business Card

On the card: (and anything else you would suggest)
- Staff member name
- Staff member position in company
- Staff member phone number
- Staff member email
- Other / Staff member Skype
- Website link

Colors
9bcb3c
abd036

Requirements
Must have
• Design of Card:
• - Green (same green as the logo)
• - Business / Corporate design
• - Something a little different / abstract that shouts premium

```html
<!DOCTYPE html>
<html lang="en">
<head>
<meta charset="utf-8">
<title>Brightpath Hosting — Business Card</title>
<link rel="stylesheet" href="https://fonts.googleapis.com/css2?family=Lato:wght@400;700;900&family=Open+Sans:wght@400;600;800&display=swap">
<style>
  :root {
    --stage: #2a2a2a;
    --card: #ffffff;
    --card-shade: #e6e6e6;
    --green: #8cc63f;
    --green-deep: #7ab52e;
    --charcoal: #3a3a3a;
    --ink: #4a4a4a;
    --rule: #7d7d7d;
    --light-text: #f4f4f4;
  }
  * { box-sizing: border-box; margin: 0; padding: 0; }
  html, body { width: 1200px; height: 997px; overflow: hidden; }
  body {
    background: var(--stage);
    font-family: "Open Sans", Arial, sans-serif;
    position: relative;
  }
  .card {
    position: absolute;
    width: 700px;
    height: 400px;
    border-radius: 22px;
    overflow: hidden;
    background: radial-gradient(ellipse at 40% 35%, var(--card) 45%, var(--card-shade) 100%);
    box-shadow: 0 18px 40px rgba(0,0,0,.55);
  }
  .card--front { left: 90px; top: 70px; }
  .card--back  { left: 410px; top: 530px; }

  /* brand lockup */
  .brand { position: absolute; display: flex; align-items: center; gap: 18px; }
  .brand__mark { width: 64px; height: 64px; background: var(--green); }
  .brand__name {
    font-family: "Open Sans", Arial, sans-serif;
    font-weight: 800;
    color: var(--green);
    font-size: 34px;
    line-height: 1;
    letter-spacing: .5px;
  }
  .card--front .brand { left: 150px; top: 120px; }
  .card--back .brand { left: 215px; top: 48px; }
  .card--back .brand__mark { width: 52px; height: 52px; }
  .card--back .brand__name { font-size: 30px; }

  /* stepped info bands */
  .row {
    position: absolute;
    height: 30px;
    display: flex;
    align-items: center;
    font-size: 15px;
    color: var(--light-text);
    letter-spacing: .3px;
  }
  .row--green { background: var(--green); }
  .row--dark  { background: var(--charcoal); }
  .row--left  { left: 0; width: 350px; justify-content: flex-end; padding-right: 22px; }
  .row--right { left: 350px; width: 350px; padding-left: 22px; }

  .card--front .row--left.r1  { top: 300px; }
  .card--front .row--left.r2  { top: 330px; }
  .card--front .row--right.r1 { top: 258px; }
  .card--front .row--right.r2 { top: 288px; }

  .card--back .row--left  { justify-content: flex-start; padding-left: 40px; }
  .card--back .row--left.r1  { top: 318px; }
  .card--back .row--left.r2  { top: 348px; }
  .card--back .row--right.r1 { top: 252px; }
  .card--back .row--right.r2 { top: 282px; }

  .icon {
    width: 20px; height: 20px; border-radius: 50%;
    display: inline-flex; align-items: center; justify-content: center;
    margin-right: 14px; flex: none;
  }
  .row--green .icon { background: var(--charcoal); }
  .row--dark .icon  { background: var(--green); }

  /* person */
  .person { position: absolute; left: 0; width: 700px; top: 196px; text-align: center; }
  .person__name { font-family: "Lato", Arial, sans-serif; font-weight: 900; font-size: 24px; color: var(--ink); }
  .person__role { font-family: "Lato", Arial, sans-serif; font-weight: 700; font-size: 13px; color: var(--green-deep); letter-spacing: .8px; margin-top: 2px; }
  .rule { position: absolute; height: 2px; background: var(--rule); }
  .rule--upper { left: 420px; top: 132px; width: 280px; }
  .rule--lower { left: 0; top: 238px; width: 240px; }
</style>
</head>
<body>

  <section class="card card--front" aria-label="Card front">
    <div class="brand">
      <span class="brand__mark"></span>
      <span class="brand__name">BRIGHTPATH<br>HOSTING</span>
    </div>
    <div class="row row--green row--left r1">Game Servers</div>
    <div class="row row--dark row--left r2">Dedicated Servers</div>
    <div class="row row--dark row--right r1">Voice Servers</div>
    <div class="row row--green row--right r2">Mitigation Security Specialists</div>
  </section>

  <section class="card card--back" aria-label="Card back">
    <div class="brand">
      <span class="brand__mark"></span>
      <span class="brand__name">BRIGHTPATH<br>HOSTING</span>
    </div>
    <span class="rule rule--upper"></span>
    <div class="person">
      <div class="person__name">Marion Feld</div>
      <div class="person__role">FOUNDER &amp; CEO</div>
    </div>
    <span class="rule rule--lower"></span>

    <div class="row row--dark row--right r1">
      <span class="icon"><svg width="10" height="10" viewBox="0 0 10 10"><circle cx="5" cy="5" r="3.5" fill="none" stroke="#fff" stroke-width="1.4"/></svg></span>/brightpathhost
    </div>
    <div class="row row--green row--right r2">
      <span class="icon"><svg width="12" height="12" viewBox="0 0 12 12"><circle cx="6" cy="6" r="4.5" fill="none" stroke="#fff" stroke-width="1.2"/><path d="M1.5 6h9M6 1.5v9" stroke="#fff" stroke-width="1"/></svg></span>www.brightpathhosting.com
    </div>
    <div class="row row--green row--left r1">
      <span class="icon"><svg width="10" height="10" viewBox="0 0 10 10"><path d="M2 1h2l1 2.5-1.2.8a5 5 0 0 0 2 2l.8-1.2L9 6v2a1 1 0 0 1-1 1A7 7 0 0 1 1 2a1 1 0 0 1 1-1z" fill="#fff"/></svg></span>+1 (555) 014-2286
    </div>
    <div class="row row--dark row--left r2">
      <span class="icon"><svg width="12" height="10" viewBox="0 0 12 10"><rect x="1" y="1.5" width="10" height="7" fill="none" stroke="#fff" stroke-width="1.2"/><path d="M1 2l5 3.5L11 2" fill="none" stroke="#fff" stroke-width="1.2"/></svg></span>hello@brightpathhosting.com
    </div>
  </section>

</body>
</html>
```